K9 Orbit needs a business card designed

We need a business card designed for K9 Orbit, an expansion of K9 Systems Pty Ltd (www.k9systems.com.au)

We provide high quality professional services for the Australian space industry. Our clients include the Southern Launch Bureau and companies working in the space industry. We identify people with space related skills both locally and internationally who are then contracted by clients to create products and support space launch activities.

Colours to be used:
- Navy blue #000080
- Rocket metallic #8A7F8D
- Platinum #E5E4E2
- Black #000000
- White #FFFFFF

*Front of the card*
I have attached our K9 Orbit logo, which needs to be the main item on the card. The 'Space' text should be placed to the right of the 'K9' part rather than below, similar to the attached K9 Systems card, which this card should match.

If subtext is included, however, it should read ‘Labour Hire • Consultancy • Project Delivery’ rather than the ‘Design • Build • Test • Maintain’ of the K9 Systems card.

A black background (rather than blue background in the K9 Systems card) might be good, with a white pattern as in the K9 Systems card. If colour is used, the logo should be in its standard colours (as provided for the K9 Orbit logo).

*Back of the card*
Include a smaller K9 Orbit logo on the back.

We need the following details for K9 Orbit personnel (as a template for entry):
- Name
- Company Position
- Mobile Number
- Email
- Office Address
- Include the K9 Orbit website: www.k9orbit.com.au

Overall, we'd like to see a design that communicates the adventure of space, professional integrity, and customer service. We look forward to seeing what you can come up with.

Target Market(s)

We provide high quality professional services for the Australian space industry. Our clients include the Southern Launch Bureau and companies working in the space industry.

Contact Information for Business Card

- Name
- Company Position
- Mobile Number
- Email
- Office Address

Requirements
Must have
• See project description.

```html
<!DOCTYPE html>
<html lang="en">
<head>
<meta charset="utf-8">
<title>K9 Orbit – Business Card</title>
<link rel="stylesheet" href="https://fonts.googleapis.com/css2?family=Montserrat:wght@600;700&family=Arimo:wght@400;700&display=swap">
<style>
  :root {
    --navy: #2b2889;
    --navy-deep: #23207a;
    --navy-emboss: #3633a0;
    --metal: #8a7f8d;
    --platinum: #e9e8f1;
    --white: #ffffff;
    --page: #2a2a2c;
    --ink-grey: #8f8a93;
  }
  * { margin: 0; padding: 0; box-sizing: border-box; }
  html, body { width: 1200px; height: 900px; overflow: hidden; }
  body {
    background: var(--page);
    font-family: "Arimo", Arial, sans-serif;
    position: relative;
  }
  .card {
    position: absolute;
    width: 720px;
    height: 411px;
    border-radius: 26px;
    overflow: hidden;
    box-shadow: 0 14px 30px rgba(0,0,0,.45);
  }

  /* Front */
  .card-front {
    left: 70px; top: 30px;
    background: linear-gradient(135deg, var(--navy) 0%, var(--navy-deep) 100%);
    color: var(--white);
  }
  .front-mark {
    position: absolute;
    left: 0; right: 0; top: 120px;
    display: flex; justify-content: center; align-items: center; gap: 18px;
    font-family: "Montserrat", sans-serif;
    font-weight: 700;
    font-size: 64px;
    letter-spacing: 6px;
    color: var(--navy-emboss);
  }
  .front-mark .dot {
    width: 22px; height: 22px; border-radius: 50%;
    background: var(--navy-emboss);
  }
  .services {
    position: absolute;
    left: 0; right: 0; top: 300px;
    text-align: center;
    font-size: 22px;
    line-height: 1.5;
    letter-spacing: .3px;
  }

  /* Back */
  .card-back {
    left: 410px; top: 460px;
    background: var(--white);
    color: var(--navy);
  }
  .back-watermark {
    position: absolute;
    right: -30px; top: 10px;
    font-family: "Montserrat", sans-serif;
    font-weight: 700;
    font-size: 96px;
    color: var(--platinum);
    white-space: nowrap;
  }
  .back-brand {
    position: absolute;
    left: 46px; top: 62px;
    display: flex; align-items: center; gap: 12px;
    font-family: "Montserrat", sans-serif;
    font-weight: 700;
    font-size: 44px;
    letter-spacing: 3px;
    color: var(--navy);
  }
  .back-brand .dot {
    width: 16px; height: 16px; border-radius: 50%;
    background: var(--metal);
  }
  .person {
    position: absolute;
    right: 46px; top: 128px;
    text-align: right;
  }
  .person .name {
    font-family: "Montserrat", sans-serif;
    font-weight: 700;
    font-size: 27px;
    color: var(--navy);
    letter-spacing: .5px;
  }
  .person .role {
    font-size: 19px;
    color: var(--ink-grey);
    margin-top: 2px;
  }
  .rule-top {
    position: absolute;
    left: 390px; right: 180px; top: 170px;
    height: 1.5px; background: var(--metal);
  }
  .address {
    position: absolute;
    right: 46px; top: 218px;
    text-align: right;
    font-size: 20px;
    line-height: 1.25;
    color: var(--ink-grey);
  }
  .rule-bottom {
    position: absolute;
    left: 46px; width: 330px; top: 268px;
    height: 1.5px; background: var(--metal);
  }
  .contacts {
    position: absolute;
    left: 46px; top: 280px;
    list-style: none;
    font-size: 22px;
    color: var(--ink-grey);
  }
  .contacts li {
    display: flex; align-items: center; gap: 12px;
    height: 34px;
  }
  .contacts .icon {
    width: 24px; height: 24px;
    border-radius: 5px;
    background: var(--navy);
    display: flex; align-items: center; justify-content: center;
    flex: none;
  }
</style>
</head>
<body>

  <section class="card card-front" aria-label="Card front">
    <div class="front-mark"><span class="dot"></span>K9 Orbit</div>
    <p class="services">Labour Hire • Consultancy • Project Delivery</p>
  </section>

  <section class="card card-back" aria-label="Card back">
    <div class="back-watermark" aria-hidden="true">K9 Orbit</div>
    <div class="back-brand"><span class="dot"></span>K9 Orbit</div>

    <div class="person">
      <div class="name">DANIEL HARTLEY</div>
      <div class="role">Manager</div>
    </div>
    <div class="rule-top"></div>

    <div class="address">Your address, city<br>state, ZIP 0000</div>

    <div class="rule-bottom"></div>
    <ul class="contacts">
      <li>
        <span class="icon">
          <svg width="14" height="14" viewBox="0 0 24 24"><path fill="#fff" d="M6.6 10.8a15 15 0 0 0 6.6 6.6l2.2-2.2c.3-.3.7-.4 1-.2 1.1.4 2.3.6 3.6.6.6 0 1 .4 1 1V20c0 .6-.4 1-1 1A17 17 0 0 1 3 4c0-.6.4-1 1-1h3.5c.6 0 1 .4 1 1 0 1.3.2 2.5.6 3.6.1.3 0 .7-.2 1z"/></svg>
        </span>
        123-456-7800
      </li>
      <li>
        <span class="icon">
          <svg width="14" height="14" viewBox="0 0 24 24"><rect x="2" y="5" width="20" height="14" rx="1.5" fill="none" stroke="#fff" stroke-width="2"/><path d="M3 6l9 7 9-7" fill="none" stroke="#fff" stroke-width="2"/></svg>
        </span>
        info@k9orbit.com.au
      </li>
      <li>
        <span class="icon">
          <svg width="14" height="14" viewBox="0 0 24 24"><circle cx="12" cy="12" r="9" fill="none" stroke="#fff" stroke-width="2"/><path d="M3 12h18M12 3c3 3 3 15 0 18M12 3c-3 3-3 15 0 18" fill="none" stroke="#fff" stroke-width="1.6"/></svg>
        </span>
        www.k9orbit.com.au
      </li>
    </ul>
  </section>

</body>
</html>
```